New italian pizza restaurant in Australia, looking for a clean and crisp new take away leaflet de...

We require a leaflet for a take away menu / introduction to the area for our new italian pizza restaurant. AS we are a brand new business we need to get the word out about opening and specials as well as a takeaway menu. I have attached logo and menu items along with a basic design concept to help speed up the process.

Target Market(s)

Widest age range possible, families

Colors

Designer to choose colors to be used in the design.

```html
<!DOCTYPE html>
<html lang="en">
<head>
<meta charset="utf-8">
<title>Corvallo Pizzeria – Grand Opening Menu</title>
<link href="https://fonts.googleapis.com/css2?family=Montserrat:wght@300;400;600;700;800;900&display=swap" rel="stylesheet">
<style>
:root{
  --bg:#16171b;
  --ink:#ececec;
  --green:#3f9157;
  --green-band:#3a9a58;
  --green-bright:#4cae68;
  --green-dark:#2f7a45;
  --mint:#6fd68d;
  --mint-ink:#3f8a55;
  --rule:#2f6b43;
  --badge:#1d1f24;
}
*{margin:0;padding:0;box-sizing:border-box}
html,body{width:927px;height:1200px;overflow:hidden;background:var(--bg)}
body{font-family:"Montserrat",sans-serif;color:var(--ink);position:relative}
.abs{position:absolute}

/* special offer */
.offer-ribbon{left:42px;top:68px;width:313px;height:46px}
.offer-ribbon span{position:absolute;left:0;right:0;top:9px;text-align:center;font-weight:800;font-size:24px;color:#fff}

.price-heads{left:392px;top:118px;display:grid;grid-template-columns:51px 47px 50px;font-size:12px;line-height:14px}
.pizza-list{left:42px;top:134px;list-style:none}
.pizza-list li{display:grid;grid-template-columns:350px 51px 47px 50px;align-items:start;font-size:11.5px;line-height:14px;height:18.4px;white-space:nowrap}
.pizza-list li.two{height:32.4px}
.pizza-list b{font-weight:700;font-size:15px;line-height:14px}
.pizza-list .p{font-size:12px}

/* hero */
.hero-clip{left:0;top:0;width:920px;height:610px;overflow:hidden}
.hero-photo{left:543px;top:57px;width:550px;height:550px;border-radius:50%;
  background:radial-gradient(circle at 55% 50%,#f1c66b 0%,#e9a84c 45%,#b45f2a 62%,#5a301a 70%,#3a2013 76%)}
.badge{left:663px;top:36px;width:186px;height:186px;border-radius:50%;background:var(--badge);
  display:flex;align-items:center;justify-content:center;text-align:center}
.badge .name{font-weight:700;font-size:19px;letter-spacing:1px;color:#fff;line-height:1.3}
.opening-art{left:0;top:0;width:927px;height:610px}
.opening-art text{font-family:"Montserrat",sans-serif;font-weight:900}

.tomato-photo{left:80px;top:1100px;width:230px;height:100px;border-radius:70px 70px 0 0;
  background:radial-gradient(ellipse at 60% 65%,#c81e12 0%,#8f130c 40%,#2f4a22 70%,rgba(22,23,27,0) 88%)}

/* lower columns */
.rule{width:1px;top:620px;height:501px;background:var(--rule)}
.col{position:absolute;font-size:11.5px;line-height:13.7px}
.col > *{position:absolute;left:0;white-space:nowrap}
.col h2{font-weight:800;font-size:25px;line-height:26px;color:var(--green)}
.col h2 small{font-size:12px;font-weight:400;color:var(--ink)}
.col h3{font-weight:700;font-size:15px;line-height:17px}
.col h3 small{font-weight:400;font-size:11.5px}
.col .item p{margin-top:-1px}
.pasta-col h2{font-size:24.5px;line-height:23px;letter-spacing:-.3px}

.address-card{left:568px;top:1019px;width:310px;height:181px}
.address-text{left:568px;top:1045px;width:310px;text-align:center;color:var(--mint-ink);font-size:17px;font-weight:300;line-height:23px}
.address-text strong{font-weight:900;font-size:18px}
.address-text .phone{color:#fff;font-weight:900;font-size:18px}
</style>
</head>
<body>

<div class="abs hero-clip">
  <div class="abs hero-photo" role="img" aria-label="Photo of a supreme pizza on a wooden board with basil leaves and parmesan shavings"></div>
  <svg class="abs opening-art" viewBox="0 0 927 610" aria-label="Grand Opening">
    <polygon points="573,305 927,220 927,297 573,385" fill="var(--green-band)"/>
    <polygon points="600,266 805,214 805,262 600,312" fill="var(--green-bright)"/>
    <text x="712" y="280" font-size="41" text-anchor="middle" fill="var(--green-dark)" transform="rotate(-14 712 266)">GRAND</text>
    <text x="750" y="330" font-size="55" text-anchor="middle" fill="#fff" transform="rotate(-14 750 312)">OPENING</text>
  </svg>
  <div class="abs badge"><span class="name">CORVALLO<br>PIZZERIA</span></div>
</div>

<svg class="abs offer-ribbon" viewBox="0 0 313 46" aria-hidden="true"><polygon points="0,0 313,0 297,23 313,46 0,46 20,23" fill="var(--green)"/></svg>
<div class="abs offer-ribbon"><span>SPECIAL OFFER</span></div>

<div class="abs price-heads"><span>Small</span><span>Large</span><span>Family</span></div>
<ol class="abs pizza-list">
  <li><span>1. <b>Capricciosa</b> – tomato, cheese, ham, mushrooms, olives</span><span class="p">$9</span><span class="p">$15</span><span class="p">$18</span></li>
  <li><span>2. <b>Napoli</b> – tomato, cheese, olives, anchovies</span><span class="p">$9</span><span class="p">$15</span><span class="p">$18</span></li>
  <li><span>3. <b>American</b> – tomato, cheese, salami</span><span class="p">$9</span><span class="p">$15</span><span class="p">$18</span></li>
  <li class="two"><span>4. <b>Vegetarian</b> – tomato, cheese, mushroom, onions,<br>capsicum, olives</span><span class="p">$9</span><span class="p">$15</span><span class="p">$18</span></li>
  <li><span>5. <b>Seafood</b> – tomato, cheese, prawns, clams, anchovies</span><span class="p">$9.5</span><span class="p">$15.5</span><span class="p">$19</span></li>
  <li><span>6. <b>The Hot One</b> – tomato, cheese, ham, salami, chilli</span><span class="p">$9</span><span class="p">$15</span><span class="p">$18</span></li>
  <li><span>7. <b>Margherita</b> – tomato, cheese, oregano</span><span class="p">$8.5</span><span class="p">$14.5</span><span class="p">$17</span></li>
  <li class="two"><span>8. <b>The Lot</b> – tomato, cheese, ham, salami, bacon,<br>mushroom, onions, capsicum, pineapple, olives</span><span class="p">$10</span><span class="p">$16</span><span class="p">$19</span></li>
  <li><span>9. <b>Mexican</b> – tomato, cheese, salami, capsicum, chilli</span><span class="p">$9</span><span class="p">$15</span><span class="p">$18</span></li>
  <li><span>10. <b>Chicken</b> – tomato, cheese, chicken, BBQ sauce</span><span class="p">$9</span><span class="p">$15</span><span class="p">$18</span></li>
  <li class="two"><span>11. <b>Meat Lovers</b> – tomato, cheese, ham, salami,<br>bacon, BBQ sauce</span><span class="p">$10</span><span class="p">$16</span><span class="p">$19</span></li>
  <li class="two"><span>12. <b>The House Pizza</b> – tomato, cheese, ham,<br>mushroom, capsicum</span><span class="p">$9</span><span class="p">$15</span><span class="p">$18</span></li>
  <li class="two"><span>13. <b>Ceaser’s Pizza</b> – tomato, cheese, ham,<br>mushroom, pineapple, prawns</span><span class="p">$10</span><span class="p">$16</span><span class="p">$19</span></li>
  <li><span>14. <b>The Breakie Pizza</b> – tomato, cheese, bacon, egg</span><span class="p">$9</span><span class="p">$15</span><span class="p">$18</span></li>
  <li class="two"><span>15. <b>The Footy Special</b> – tomato, cheese, ham,<br>capsicum, onions, pineapple</span><span class="p">$9</span><span class="p">$15</span><span class="p">$18</span></li>
  <li class="two"><span>16. <b>The Corvallo</b> – tomato, cheese ham,<br>mushrooms, onions, olives</span><span class="p">$9</span><span class="p">$15</span><span class="p">$18</span></li>
  <li class="two"><span>17. <b>The Corvo Special</b> – tomato, cheese, ham,<br>onions, bacon, egg</span><span class="p">$10</span><span class="p">$16</span><span class="p">$19</span></li>
  <li><span>18. <b>Ham</b> - tomato, cheese, ham</span><span class="p">$8.5</span><span class="p">$14.5</span><span class="p">$17</span></li>
  <li><span>19. <b>Garlic</b> – garlic, cheese, oregano</span><span class="p">$8.5</span><span class="p">$14.5</span><span class="p">$17</span></li>
</ol>

<div class="abs tomato-photo" role="img" aria-label="Photo of cherry tomatoes, basil leaves and parmesan"></div>

<div class="abs rule" style="left:298px"></div>
<div class="abs rule" style="left:568px"></div>

<section class="col mains-col" style="left:44px;top:0">
  <h2 style="top:618px">MAIN MEALS</h2>
  <p style="top:650px">(all mains served with chips or salad)</p>
  <div class="item" style="top:680px"><h3>Scotch Fillet Steak 300g <small>$25</small></h3><p>grass fed, with your choice of Mushroom,<br>Pepper or Garlic sauce</p></div>
  <div class="item" style="top:740px"><h3>Calamari <small>$19.5</small></h3><p>Flash fried or crumbed squid with aioli</p></div>
  <div class="item" style="top:786px"><h3>Chicken Parmigiana <small>$19.5</small></h3><p>Schnitzel topped with ham, Napoli sauce<br>&amp; mozzarella</p></div>
  <div class="item" style="top:846px"><h3>Veal Scallopini <small>- with your choice of</small></h3><p>mushroom or creamy avocado sauce $19.5</p></div>
  <div class="item" style="top:892px"><h3>Veal Parmigiana <small>-schnitzel topped</small></h3><p>ham, Napoli sauce &amp; mozzarella $19.5</p></div>
  <h2 style="top:947px">KIDS MENU <small>$9.5</small></h2>
  <p style="top:972px">Pasta Bolognese<br>Pasta Napoli<br>Chicken Nuggets &amp; Chips<br>Cheeseburger &amp; Chips</p>
  <h2 style="top:1049px">SIDES</h2>
  <p style="top:1073px">Garlic Bread $4.5<br>Chips $7.5<br>Garden Salad $5</p>
</section>

<section class="col salads-col" style="left:328px;top:0">
  <h2 style="top:618px">SALADS</h2>
  <div class="item" style="top:648px"><h3>Greek Salad <small>– cos lettuce, tomato,</small></h3><p>onion, cucumber, olives, feta cheese &amp;<br>dressing $14.5</p></div>
  <div class="item" style="top:707px"><h3>Grilled Chicken Salad <small>–</small></h3><p>Seasoned chicken, mixed leaves, cherry<br>tomato, Spanish onion, cucumber with<br>garlic infused olive oil $15.5</p></div>
  <div class="item" style="top:782px"><h3>Chicken Ceasar Salad <small>– Chicken,</small></h3><p>cos lettuce, croutons, shaved parmesan,<br>anchovies, egg, bacon served with ceaser<br>dressing $15.5</p></div>
  <h2 style="top:869px">DESSERTS</h2>
  <p style="top:894px">Gelati 500mls Varieties $6.5<br>Baci $6<br>Tartufo $6<br>Chocolate Mousse $6</p>
  <h2 style="top:972px">DRINKS</h2>
  <p style="top:996px">Soft drinks 375ml - $2.5<br>Soft drinks 1.25L - $4.5<br>Water 600ml - $2.5</p>
  <h2 style="top:1060px">COMBO DEALS</h2>
  <p style="top:1085px">Any 2 Family pizzas, garlic bread and<br>1.25l soft drink - $41.00<br>1 Large pizza, 1 pasta, garlic bread and<br>1.25l soft drink - $38.00<br>2 Large pizzas, 1 garlic bread and 1.25l<br>soft drink - $36.00</p>
</section>

<section class="col pasta-col" style="left:591px;top:0">
  <h2 style="top:613px">PASTA- SPAGHETTI,<br>PENNE, GNOCCHI,<br>FETTUCINE, LINGUINE</h2>
  <div class="item" style="top:691px"><h3>Bolognese <small>– traditional Italian meat sauce $14</small></h3></div>
  <div class="item" style="top:723px"><h3>Carbonara<small>- onion, bacon, egg in creamy</small></h3><p>parmesan cheese sauce $14</p></div>
  <div class="item" style="top:769px"><h3>Napolitana <small>– traditional Italian Napoli sauce $13.5</small></h3></div>
  <div class="item" style="top:801px"><h3>Amatriciana <small>– bacon, onion, olives, capsicum,</small></h3><p>fresh chili cooked in Napoli sauce $15</p></div>
  <div class="item" style="top:848px"><h3>Marinara <small>– mussels, prawns, calamari, scallops</small></h3><p>cooked in Napoli sauce $15</p></div>
  <div class="item" style="top:894px"><h3>Risotto Polo <small>– chicken, mushroom, onion,</small></h3><p>cooked in a cream sauce &nbsp; $16.5</p></div>
  <div class="item" style="top:941px"><h3>Lasagna <small>– Homemade Lasagna $15</small></h3></div>
  <div class="item" style="top:973px"><h3>Pasta Your way<small>- choose any three ingredients</small></h3><p>with cream or Napoli sauce $14.5</p></div>
</section>

<svg class="abs address-card" viewBox="0 0 310 181" aria-hidden="true"><polygon points="0,47 155,0 310,47 310,181 0,181" fill="var(--mint)"/></svg>
<div class="abs address-text">
  <div>Address:</div>
  <strong>12 HARROW LANE,<br>BRINDALE 3061</strong>
  <div>Tel: <span class="phone">000 000 000 00</span></div>
  <div>Website/ Online ordering:</div>
  <strong>ORDERCORVALLO.COM</strong>
</div>

</body>
</html>
```